Lakeshore Youngsters Circle Business Card Project

We are a Minneapolis based discount club that caters to families with children. We need a business card that can be used to communicate our contact information to other businesses that may wish to offer discounts on our website.

Please use placeholders for contact information (i.e. John Doe, 123 Any Street, Any Town, etc.) and include spaces for the following: Full name, title, email, phone number, website, one line street address, city, state, and zip code.
Updates

Reason: I have extended the deadline because I had not intended the project to close so quickly.

Target Market(s)

Most of the time the business cards will be used in business to business situations. However, from time to time they may be distributed to our end customer, families with children.

Industry/Entity Type

Club

Font styles to use
Serif
Sans Serif
Other font styles liked:
• Open to suggestions

Requirements
Nice to have
• We might use the reverse side of the card as the design for our membership card.

```html
<!DOCTYPE html>
<html lang="en">
<head>
<meta charset="utf-8">
<title>Lakeshore Youngsters Circle – Business Card</title>
<link rel="stylesheet" href="https://fonts.googleapis.com/css2?family=Ubuntu:wght@400;500&display=swap">
<style>
  :root {
    --lime: #7cfc02;
    --lime-light: #a9fd2c;
    --lime-deep: #66e000;
    --name-green: #6ad600;
    --white: #ffffff;
    --mark-green: #4fbf00;
    --shadow: rgba(0, 60, 0, 0.35);
  }
  html, body {
    margin: 0;
    padding: 0;
    width: 1200px;
    height: 720px;
    overflow: hidden;
    background: var(--lime);
  }
  .card {
    position: relative;
    width: 1200px;
    height: 720px;
    overflow: hidden;
    background: var(--lime);
    font-family: "Ubuntu", sans-serif;
  }
  .top-shade {
    position: absolute;
    left: 0; top: 0;
    width: 1200px; height: 149px;
    background: linear-gradient(to bottom, var(--lime) 0%, #6fe400 100%);
  }
  .accent-stripe {
    position: absolute;
    left: 709px; top: 0;
    width: 366px; height: 720px;
    background: var(--lime-light);
  }
  .name-band {
    position: absolute;
    left: 0; top: 149px;
    width: 1200px; height: 148px;
    background: var(--white);
    box-shadow: 0 6px 14px var(--shadow);
  }
  .person-name {
    position: absolute;
    left: 82px; top: 172px;
    margin: 0;
    font-size: 49px;
    font-weight: 400;
    line-height: 1;
    color: var(--name-green);
  }
  .person-title {
    position: absolute;
    left: 82px; top: 230px;
    margin: 0;
    font-size: 36px;
    font-weight: 400;
    line-height: 1;
    color: var(--name-green);
  }
  .contact-panel {
    position: absolute;
    left: 41px; top: 345px;
    width: 615px; height: 332px;
    box-sizing: border-box;
    border-radius: 28px;
    background: var(--lime-deep);
    border: 2px solid rgba(255, 255, 255, 0.85);
    box-shadow: 0 0 12px rgba(255, 255, 255, 0.8);
    padding: 50px 0 0 20px;
  }
  .contact-list {
    list-style: none;
    margin: 0;
    padding: 0;
    color: var(--white);
    font-size: 32px;
    line-height: 43px;
    white-space: nowrap;
  }
  .brand-tile {
    position: absolute;
    left: 668px; top: 75px;
    width: 470px; height: 344px;
    border-radius: 20px;
    background: var(--white);
    box-shadow: 0 4px 16px var(--shadow);
    display: flex;
    align-items: center;
    justify-content: center;
    gap: 18px;
  }
  .brand-dot {
    width: 42px; height: 42px;
    flex: none;
  }
  .brand-name {
    margin: 0;
    font-size: 44px;
    font-weight: 500;
    line-height: 1.1;
    color: var(--mark-green);
  }
</style>
</head>
<body>
  <div class="card">
    <div class="top-shade"></div>
    <div class="accent-stripe"></div>
    <div class="name-band"></div>

    <h1 class="person-name">Daniel Reyes</h1>
    <p class="person-title">President</p>

    <div class="contact-panel">
      <ul class="contact-list">
        <li>Address: 48 Harbor Lane, MN, 55401</li>
        <li>Phone: 612 555 0142</li>
        <li>Fax: 612 555 0143</li>
        <li>E-mail: hello@lakeshorecircle.com</li>
        <li>Web: www.lakeshorecircle.com/join</li>
      </ul>
    </div>

    <div class="brand-tile">
      <svg class="brand-dot" viewBox="0 0 42 42" aria-hidden="true">
        <circle cx="21" cy="21" r="21" fill="var(--mark-green)"/>
      </svg>
      <p class="brand-name">Lakeshore<br>Youngsters<br>Circle</p>
    </div>
  </div>
</body>
</html>
```